Business Card, A4 Letter Head and DL Envelope for Vantrelle

We are looking for a design for our Business Card, A4 Letter Head and DL Envelope.

Vantrelle is a distributor of promotional products. We specialize in a range of branded promotional products, these include pens, polo shirts, key rings, drink bottles, uniforms and bags to name a few. We are experts in marketing and assist companies in choosing the right promotional product for their needs. We will predominately be an online business where customers visit our website and browse our range of promotional products and branding options.

Our colours are black, red, white and grey.

Files must be supplied in eps, pdf and ai format.

Please display the following information:
Corbin Hale
Account Manager
Suite xxx, 214 Dawlish Parade Melbourne, Victoria 3000
Phone +61 3 5550 1827
Mobile +61 455 501 936
sales@vantrelle.com.au
www.vantrelle.com.au

```html
<!DOCTYPE html>
<html lang="en">
<head>
<meta charset="utf-8">
<title>Vantrelle DL Envelope</title>
<link href="https://fonts.googleapis.com/css2?family=Questrial&display=swap" rel="stylesheet">
<style>
  :root {
    --backdrop: #6a6a6a;
    --paper: #ffffff;
    --red: #d71f26;
    --red-deep: #bd1c23;
    --red-bright: #ec1c24;
    --ink: #222222;
    --grey: #6d6e70;
  }
  * { margin: 0; padding: 0; box-sizing: border-box; }
  html, body { width: 1200px; height: 1110px; overflow: hidden; }
  body {
    background: radial-gradient(ellipse at 50% 40%, #727272 0%, var(--backdrop) 70%, #5c5c5c 100%);
    font-family: "Questrial", "Century Gothic", sans-serif;
    position: relative;
  }
  .envelope {
    position: absolute;
    left: 125px;
    width: 960px;
    background: var(--paper);
    box-shadow: 0 4px 6px rgba(0,0,0,0.35);
    overflow: hidden;
  }
  .envelope--front { top: 52px; height: 415px; }
  .envelope--back { top: 613px; height: 420px; }
  .envelope svg.artwork { position: absolute; inset: 0; display: block; }

  .sender {
    position: absolute;
    left: 69px;
    top: 124px;
  }
  .brand {
    display: flex;
    align-items: center;
    gap: 8px;
    height: 44px;
  }
  .brand__dot {
    width: 36px; height: 36px;
    border-radius: 50%;
    background: var(--red);
  }
  .brand__name {
    font-size: 22px;
    letter-spacing: 0.5px;
    color: var(--grey);
    text-transform: uppercase;
  }
  .sender__details {
    margin-top: 14px;
    margin-left: 5px;
    padding-left: 8px;
    border-left: 1.5px solid var(--red);
    font-size: 10.5px;
    line-height: 13.5px;
  }
  .contact-line { color: var(--ink); }
  .contact-line__label { color: var(--red); display: inline-block; width: 12px; }
  .address { color: var(--red); margin-top: 4px; }
</style>
</head>
<body>

<section class="envelope envelope--front" aria-label="Envelope front">
  <svg class="artwork" viewBox="0 0 960 415" width="960" height="415" aria-hidden="true">
    <path d="M0 0 H960 V56 C640 60 240 80 0 123 Z" fill="var(--red-bright)"/>
    <path d="M0 0 H960 V56 C700 58 400 66 0 123 Z" fill="var(--red)"/>
    <path d="M0 0 H960 V12 C620 18 300 34 0 56 Z" fill="var(--red-deep)"/>
    <rect x="0" y="408" width="960" height="7" fill="var(--red)"/>
  </svg>

  <div class="sender">
    <div class="brand">
      <span class="brand__dot"></span>
      <span class="brand__name">Vantrelle</span>
    </div>
    <div class="sender__details">
      <div class="contact-line"><span class="contact-line__label">M</span>+61 455 501 936</div>
      <div class="contact-line"><span class="contact-line__label">T</span>+61 3 5550 1827</div>
      <div class="contact-line"><span class="contact-line__label">e</span>sales@vantrelle.com.au</div>
      <div class="address">Suite xxx, 214 Dawlish Parade<br>Melbourne, Victoria 3000</div>
    </div>
  </div>
</section>

<section class="envelope envelope--back" aria-label="Envelope back">
  <svg class="artwork" viewBox="0 0 960 420" width="960" height="420" aria-hidden="true">
    <path d="M0 0 H960 V44 A30 30 0 0 1 930 74 H30 A30 30 0 0 1 0 44 Z" fill="var(--red)"/>
    <path d="M0 0 H960 V12 C640 18 300 34 0 56 Z" fill="var(--red-deep)"/>
    <path d="M0 420 V413 A30 30 0 0 1 30 394 H930 A30 30 0 0 1 960 413 V420 Z" fill="var(--red-deep)"/>
  </svg>
</section>

</body>
</html>
```